Powerpoint design for management consultant

We need a powerpoint design to use for our corporate presentations, proposal summaries and for delivering report recommendations.

Target Market(s)

Executives in Government & Private Industry

Industry/Entity Type

Consultant

Requirements
Must have
• Must use the company logo contained in the uploaded files.
Must be a powerpoint template file (.potx) that can be used with Powerpoint 2007 and later.
Must have a title slide.
Must have a purpose slide (in today's presentation we will cover ....)
Must have an agenda slide.
Must have three topic slides (topic1, topic2, topic3) as transition slides
Must support side by side comparisons
Any images used must be available royalty/ license free
Must have a summary slide.
Must have a questions slide at the end.
Must have a footer containing slide number in format of x of y.
Must have a footer containing presentation name.
Must have a footer containing the presentation date.
Must have a footer containing "confidential"
Nice to have
• The powerpoint should support the ability to represent data using infographics.
Should not have
• no tag lines or references to being management consultants. must not use custom fonts.

```html
<!DOCTYPE html>
<html lang="en">
<head>
<meta charset="utf-8">
<title>Corporate Presentation Template</title>
<link href="https://fonts.googleapis.com/css2?family=Carlito:wght@400;700&display=swap" rel="stylesheet">
<style>
:root{
  --navy:#0d2b45;
  --orange:#f7a81b;
  --teal:#4dbfad;
  --cyan:#2ab9d9;
  --magenta:#b8479a;
  --ice:#d3eef5;
  --ink:#1f2a33;
  --grey:#8a8f94;
  --panel:#eef0f2;
  --white:#ffffff;
}
*{box-sizing:border-box;margin:0;padding:0}
html,body{width:1200px;height:900px;overflow:hidden;background:var(--white)}
body{position:relative;font-family:"Carlito","Calibri",sans-serif;color:var(--ink)}
.slide{position:absolute;width:378px;height:284px;background:var(--white);overflow:hidden;
  box-shadow:1px 2px 5px rgba(0,0,0,.35)}
.c1{left:16px}.c2{left:407px}.c3{left:798px}
.r1{top:11px}.r2{top:307px}.r3{top:603px}

.stripes{position:absolute;background:
  linear-gradient(125deg,var(--navy) 0%,#2a4a6e 22%,#5a3f7a 38%,var(--navy) 52%,#1d5a72 68%,#6a3a72 82%,var(--navy) 100%)}
.stripes.soft{background:linear-gradient(120deg,#1d5a72 0%,#5a3f7a 40%,#7a4a3a 65%,var(--navy) 100%)}

/* content slide chrome */
.header{position:absolute;left:0;top:0;width:100%;height:40px;background:var(--navy);border-bottom:3px solid var(--orange)}
.header .stripes{left:0;top:0;width:110px;height:37px}
.header h2{position:absolute;right:12px;top:9px;font-weight:400;font-size:17px;color:var(--white)}
.footer{position:absolute;left:0;bottom:0;width:100%;height:9px;background:var(--teal);
  font-size:5.5px;color:var(--white);line-height:9px}
.footer span{position:absolute}
.footer .date{left:10px}.footer .name{left:165px}.footer .conf{left:293px}.footer .num{right:10px}
.brand{position:absolute;font-weight:700;letter-spacing:.5px;display:flex;align-items:center;gap:3px}
.brand i{display:block;background:var(--cyan)}
.brand.small{right:8px;bottom:13px;font-size:11px;color:var(--navy)}
.brand.small i{width:6px;height:6px}
.brand.large{right:18px;top:20px;font-size:18px;color:var(--white)}
.brand.large i{width:9px;height:9px}

/* title slide */
.cover .stripes{left:0;top:0;width:100%;height:213px}
.cover .rule{position:absolute;left:342px;top:212px;width:60px;height:3px;background:var(--orange);transform:rotate(38deg);transform-origin:left}
.cover h1{position:absolute;left:16px;top:229px;font-weight:400;font-size:17px;color:var(--navy)}
.cover p{position:absolute;left:16px;top:253px;font-size:10.5px;color:var(--grey)}

/* purpose */
.purpose .lead{position:absolute;left:12px;top:53px;font-size:10.5px;color:var(--magenta)}
.bullets{list-style:none;font-size:10px;line-height:1.3}
.bullets li{position:relative;padding-left:14px;margin-bottom:6px}
.bullets li::before{content:"";position:absolute;left:2px;top:4px;border-left:4px solid var(--magenta);border-top:3px solid transparent;border-bottom:3px solid transparent}
.bullets li.sub{padding-left:32px;font-size:8.5px;margin-bottom:5px}
.bullets li.sub::before{left:19px;top:5px;width:6px;height:1px;border:0;background:var(--magenta)}
.purpose .bullets{position:absolute;left:12px;top:70px;width:355px}

/* topic */
.topic{background:var(--navy)}
.topic .stripes{left:0;top:0;width:100%;height:100%}
.topic .band{position:absolute;left:0;top:111px;width:100%;height:61px;background:var(--orange)}
.topic .band h2{position:absolute;left:18px;top:19px;font-weight:400;font-size:20px;color:var(--navy)}

/* agenda */
.agenda-list{position:absolute;left:6px;top:56px;width:364px;list-style:none}
.agenda-list li{position:relative;height:22px;margin-bottom:11px}
.agenda-list .n{position:absolute;left:0;top:1px;width:20px;height:20px;background:var(--cyan);color:var(--white);
  font-size:10px;font-weight:700;text-align:center;line-height:20px;clip-path:polygon(25% 0,100% 0,100% 100%,25% 100%,0 50%)}
.agenda-list p{position:absolute;left:16px;top:2px;right:0;height:18px;background:var(--ice);
  border-bottom:2px solid #9fd7e5;font-size:5.6px;line-height:1.25;padding:2px 4px 0 9px;color:var(--navy)}

/* comparison */
.col{position:absolute;top:55px;width:170px}
.col.a{left:12px}.col.b{left:198px}
.col h3{font-size:11px;font-weight:700;color:var(--magenta);margin-bottom:8px}
.col .bullets{font-size:9.2px}
.col .bullets li.sub{font-size:7.8px}
.divider{position:absolute;left:189px;top:58px;height:196px;border-left:1px dotted var(--magenta)}

/* graphic */
.graphic .lead{position:absolute;left:0;width:100%;top:53px;text-align:center;font-size:10.5px;color:var(--magenta)}
.graphic .panel{position:absolute;left:18px;top:85px;width:342px;height:155px;background:var(--panel)}
.graphic .bar{position:absolute;left:18px;top:240px;width:342px;height:8px;background:var(--orange)}
.graphic .note{position:absolute;left:18px;top:85px;width:82px;height:155px;background:var(--navy);color:var(--white);
  font-size:6.6px;line-height:1.3;padding:8px 6px}
.graphic .note p+p{margin-top:7px}
.graphic .note::after{content:"";position:absolute;right:-5px;top:70px;border-left:5px solid var(--navy);border-top:5px solid transparent;border-bottom:5px solid transparent}
.graphic svg{position:absolute;left:160px;top:86px}

/* questions */
.questions .visual{position:absolute;left:110px;top:72px;width:158px;height:182px;
  background:linear-gradient(160deg,#f4f4f4,#c9c9c9 55%,#f2f2f2)}

/* closing */
.closing .stripes{left:0;top:0;width:100%;height:205px}
.closing .rule{position:absolute;left:344px;top:204px;width:60px;height:3px;background:var(--orange);transform:rotate(38deg);transform-origin:left}
.closing h2{position:absolute;left:0;width:100%;top:231px;text-align:center;font-weight:400;font-size:15px;color:var(--navy)}
.closing p{position:absolute;left:0;width:100%;top:253px;text-align:center;font-size:10.5px;color:var(--grey)}
</style>
</head>
<body>

<!-- Title -->
<section class="slide cover c1 r1">
  <div class="stripes" role="img" aria-label="Diagonal stripe pattern in cyan, magenta and orange on navy"></div>
  <div class="brand large"><i></i>Vantrell</div>
  <div class="rule"></div>
  <h1>Presentation title</h1>
  <p>Lorem ipsum dolor sit amet</p>
</section>

<!-- Purpose -->
<section class="slide purpose c2 r1">
  <header class="header"><div class="stripes" role="img" aria-label="Diagonal stripe pattern"></div><h2>Purpose slide</h2></header>
  <p class="lead">IN TODAY'S PRESENTATION WE WILL COVER:</p>
  <ul class="bullets">
    <li>In id libero adipiscing, ultricies magna quis, fermentum sem. Donec porta volutpat sollicitudin.</li>
    <li>Nullam at ante libero. Suspendisse vitae malesuada arcu. Ut non hendrerit diam.</li>
    <li class="sub">Aenean mattis felis neque.</li>
    <li class="sub">Proin porta est nisi, sed laoreet nibh fermentum vel.</li>
    <li>Etiam pretium tellus diam, in fermentum enim congue non.</li>
    <li class="sub">Pellentesque lectus nisl, vulputate vel tincidunt nec, tempor eu massa.</li>
    <li class="sub">Interdum et malesuada fames ac ante ipsum primis in faucibus.</li>
    <li>Vivamus vehicula condimentum mollis. Aliquam in aliquam.</li>
  </ul>
  <div class="brand small"><i></i>Vantrell</div>
  <footer class="footer"><span class="date">23-10-2013</span><span class="name">Presentation Title</span><span class="conf">Confidential</span><span class="num">2</span></footer>
</section>

<!-- Topic -->
<section class="slide topic c3 r1">
  <div class="stripes" role="img" aria-label="Diagonal stripe pattern in cyan, magenta and orange on navy"></div>
  <div class="brand large"><i></i>Vantrell</div>
  <div class="band"><h2>TOPIC 1</h2></div>
</section>

<!-- Agenda -->
<section class="slide agenda c1 r2">
  <header class="header"><div class="stripes" role="img" aria-label="Diagonal stripe pattern"></div><h2>Agenda slide</h2></header>
  <ol class="agenda-list">
    <li><span class="n">1</span><p>Lorem ipsum dolor sit amet, consectetur adipiscing elit. In id libero adipiscing, ultricies magna quis, fermentum sem. Donec porta volutpat sollicitudin. Ut libero ante, elementum sit amet urna in, commodo interdum tellus.</p></li>
    <li><span class="n">2</span><p>Lorem ipsum dolor sit amet, consectetur adipiscing elit. In id libero adipiscing, ultricies magna quis, fermentum sem. Donec porta volutpat sollicitudin. Ut libero ante, elementum sit amet urna in, commodo interdum tellus.</p></li>
    <li><span class="n">3</span><p>Lorem ipsum dolor sit amet, consectetur adipiscing elit. In id libero adipiscing, ultricies magna quis, fermentum sem. Donec porta volutpat sollicitudin. Ut libero ante, elementum sit amet urna in, commodo interdum tellus.</p></li>
    <li><span class="n">4</span><p>Lorem ipsum dolor sit amet, consectetur adipiscing elit. In id libero adipiscing, ultricies magna quis, fermentum sem. Donec porta volutpat sollicitudin. Ut libero ante, elementum sit amet urna in, commodo interdum tellus.</p></li>
    <li><span class="n">5</span><p>Lorem ipsum dolor sit amet, consectetur adipiscing elit. In id libero adipiscing, ultricies magna quis, fermentum sem. Donec porta volutpat sollicitudin. Ut libero ante, elementum sit amet urna in, commodo interdum tellus.</p></li>
    <li><span class="n">6</span><p>Lorem ipsum dolor sit amet, consectetur adipiscing elit. In id libero adipiscing, ultricies magna quis, fermentum sem. Donec porta volutpat sollicitudin. Ut libero ante, elementum sit amet urna in, commodo interdum tellus.</p></li>
  </ol>
  <div class="brand small"><i></i>Vantrell</div>
  <footer class="footer"><span class="date">23-10-2013</span><span class="name">Presentation Title</span><span class="conf">Confidential</span><span class="num">5</span></footer>
</section>

<!-- Comparison -->
<section class="slide compare c2 r2">
  <header class="header"><div class="stripes" role="img" aria-label="Diagonal stripe pattern"></div><h2>Comparison slide</h2></header>
  <div class="col a">
    <h3>Theme A</h3>
    <ul class="bullets">
      <li>Nam sed placerat lectus, id porttitor purus.</li>
      <li class="sub">Maecenas cursus, sapien sit amet semper pellentesque, odio enim dictum dolor, vitae malesuada est libero malesuada mauris.</li>
      <li class="sub">Proin nec faucibus quam. Pellentesque tincidunt aliquet hendrerit.</li>
      <li>Etiam augue urna, venenatis eu placerat ut, tincidunt non risus. Nam mattis tempor mi.</li>
    </ul>
  </div>
  <div class="divider"></div>
  <div class="col b">
    <h3>Theme B</h3>
    <ul class="bullets">
      <li>Curabitur id suscipit elit.</li>
      <li>Fusce molestie, lorem quis porttitor sodales, felis ipsum commodo nisi, nulla et diam.</li>
      <li>Aenean tempus facilisis eleifend.</li>
      <li class="sub">Aenean ut arcu non tellus adipiscing porttitor nunc.</li>
      <li class="sub">Pellentesque porttitor turpis ligula, vel elit luctus pretium.</li>
      <li class="sub">Donec risus ante, dignissim in consectetur nulla.</li>
    </ul>
  </div>
  <div class="brand small"><i></i>Vantrell</div>
  <footer class="footer"><span class="date">23-10-2013</span><span class="name">Presentation Title</span><span class="conf">Confidential</span><span class="num">7</span></footer>
</section>

<!-- Graphic -->
<section class="slide graphic c3 r2">
  <header class="header"><div class="stripes" role="img" aria-label="Diagonal stripe pattern"></div><h2>Graphic slide</h2></header>
  <p class="lead">Nam sed placerat lectus, id porttitor purus.</p>
  <div class="panel"></div>
  <div class="bar"></div>
  <div class="note">
    <p>Lorem ipsum dolor sit amet, consectetur adipiscing elit. In id libero adipiscing, ultricies magna quis, fermentum sem.</p>
    <p>Donec porta volutpat sollicitudin. Nullam at ante libero. Suspendisse vitae malesuada arcu. Ut non hendrerit diam.</p>
  </div>
  <svg width="154" height="154" viewBox="0 0 154 154" aria-label="Doughnut chart">
    <g transform="rotate(-90 77 77)" fill="none" stroke-width="35">
      <circle cx="77" cy="77" r="52" stroke="var(--magenta)" stroke-dasharray="191.4 326.7" stroke-dashoffset="0"/>
      <circle cx="77" cy="77" r="52" stroke="var(--cyan)" stroke-dasharray="74.7 326.7" stroke-dashoffset="-191.4"/>
      <circle cx="77" cy="77" r="52" stroke="var(--teal)" stroke-dasharray="32.7 326.7" stroke-dashoffset="-266.1"/>
      <circle cx="77" cy="77" r="52" stroke="var(--orange)" stroke-dasharray="28 326.7" stroke-dashoffset="-298.8"/>
    </g>
    <g fill="#fff" font-size="9" font-family="Carlito, sans-serif" text-anchor="middle">
      <text x="124" y="101">8,2</text>
      <text x="28" y="103">3,2</text>
      <text x="38" y="53">1,4</text>
      <text x="64" y="39">1,2</text>
    </g>
  </svg>
  <div class="brand small"><i></i>Vantrell</div>
  <footer class="footer"><span class="date">23-10-2013</span><span class="name">Presentation Title</span><span class="conf">Confidential</span><span class="num">8</span></footer>
</section>

<!-- Questions -->
<section class="slide questions c1 r3">
  <header class="header"><div class="stripes" role="img" aria-label="Diagonal stripe pattern"></div><h2>Questions slide</h2></header>
  <div class="visual" role="img" aria-label="Grey three-dimensional question mark maze illustration"></div>
  <div class="brand small"><i></i>Vantrell</div>
  <footer class="footer"><span class="date">23-10-2013</span><span class="name">Presentation Title</span><span class="conf">Confidential</span><span class="num">9</span></footer>
</section>

<!-- Closing -->
<section class="slide closing c2 r3">
  <div class="stripes" role="img" aria-label="Diagonal stripe pattern in cyan, magenta and orange on navy"></div>
  <div class="brand large"><i></i>Vantrell</div>
  <div class="rule"></div>
  <h2>THANK YOU</h2>
  <p>FOR YOUR TIME</p>
</section>

</body>
</html>
```